Design for mobile and web app for sweepstakes.

We need the design for a mobile app (planned to be build with jquery mobile) and web app (mobile first, we will use same look and feel as mobile just with displaying more info at once).

The following pages must be included:
- Userregistration/Login (Reg via Email, Chatnook-Reg)

- List of available sweepstakes (including some icons: a video icon, a "like button" type icon, a "provide some info" type of icon) this should be on the side in wep app but in mobile app its a list. possible is also a mobile display where users can swipe back and forth through it.

- single sweepstake detailview . should present a single sweepstake and give users the opportunity to participate with a button.

user settings. (doesnt not have to include a lot of fields we will at ourself. should contain some datepicker (birthday), some on/off switch (receive newsletters) some textfield in order for us to have a feel.

We have included the following files:
- prizewell_logo_final01.png:
this is our logo which should be used and also the look and feel must fit with the logo.

- prizewell_logo_final06.png:
this is the app-icon

this is a simple mockup for a registration page. the design doesnt have to contain all fields we will do that ourselfes starting from your handover, but should represent a common registration page with some fields

this is just a mockup for a possible design. not that it does use our old logo. This again is not binding is just to get a feel for what we are looking for. A list of sweepstakes and a detailspage for the sweepstake for users to participate in it.

Target Market(s)

German speaking users, Austria, Germany, Switzerland
The app is adressing a wide crowd of users who are interested in participating in sweepstakes.

Industry/Entity Type

Build

Number of Pages Required

4 page

Font styles to use
Sans Serif

Requirements
Must have
• - jquery and jquery mobile
• - html5 (preferable bootstrap-based)
• - css3
• - description on used fonts and colors. fonts must be free to use and publicly available for anyone to use.
• - all buttons should be css

```html
<!DOCTYPE html>
<html lang="en">
<head>
<meta charset="utf-8">
<title>prizewell – Login</title>
<link href="https://fonts.googleapis.com/css2?family=Roboto:wght@400;700&display=swap" rel="stylesheet">
<style>
  :root {
    --brand-green: #72a333;
    --ink: #111111;
    --paper: #ffffff;
    --field-text: #ffffff;
  }
  * { box-sizing: border-box; margin: 0; padding: 0; }
  html, body {
    width: 755px;
    height: 1200px;
    overflow: hidden;
    background: var(--paper);
    font-family: "Roboto", Arial, sans-serif;
  }
  .login-screen {
    position: relative;
    width: 755px;
    height: 1200px;
  }
  .brand {
    position: absolute;
    top: 352px;
    left: 0;
    width: 755px;
    display: flex;
    justify-content: center;
    align-items: center;
    gap: 16px;
  }
  .brand-dot {
    width: 30px;
    height: 30px;
    border-radius: 50%;
    background: var(--brand-green);
  }
  .brand-name {
    font-size: 66px;
    font-weight: 700;
    color: var(--ink);
    letter-spacing: -1px;
    line-height: 1;
  }
  .login-form {
    position: absolute;
    top: 592px;
    left: 148px;
    width: 463px;
  }
  .field {
    display: block;
    width: 100%;
    height: 55px;
    border: none;
    outline: none;
    background: var(--brand-green);
    color: var(--field-text);
    font-family: inherit;
    font-size: 28px;
    padding: 0 16px;
    margin-bottom: 35px;
  }
  .field::placeholder { color: var(--field-text); opacity: 1; }
  .actions {
    display: flex;
    height: 55px;
    margin-top: -3px;
  }
  .btn {
    flex: 1;
    border: none;
    font-family: inherit;
    font-size: 28px;
    color: var(--field-text);
    cursor: pointer;
  }
  .btn-signup { background: var(--ink); }
  .btn-login { background: var(--brand-green); }
</style>
</head>
<body>
  <main class="login-screen">
    <header class="brand">
      <span class="brand-dot"></span>
      <span class="brand-name">prizewell</span>
    </header>
    <form class="login-form">
      <input class="field field-email" type="email" placeholder="email">
      <input class="field field-password" type="password" placeholder="Password">
      <div class="actions">
        <button class="btn btn-signup" type="button">signup</button>
        <button class="btn btn-login" type="submit">login</button>
      </div>
    </form>
  </main>
</body>
</html>
```